TRV PowerPoint

I am looking for a clean, corporate PowerPoint template.

I would like the following:
- title slide
- break slide
- blank slide with title (for graphs or graphics)
- an ending slide.

Target Market(s)

Business professionals, medium to large business clients.

Requirements
Must have
• Must incorporate the TRV logo in either the header or footer

```html
<!DOCTYPE html>
<html lang="en">
<head>
<meta charset="utf-8">
<title>TRV PowerPoint – Content Slide</title>
<link rel="stylesheet" href="https://fonts.googleapis.com/css2?family=Graduate&family=Source+Sans+3:wght@400;600&family=Arimo&display=swap">
<style>
  :root {
    --sky: #29a8e0;
    --deep-blue: #0b72b9;
    --charcoal: #222222;
    --paper-light: #f1f1f1;
    --paper-mid: #d6d6d6;
    --white: #ffffff;
    --logo-blue: #1a6fb8;
  }
  * { margin: 0; padding: 0; box-sizing: border-box; }
  html, body { width: 1200px; height: 900px; overflow: hidden; background: var(--white); }
  body { position: relative; font-family: "Source Sans 3", "Myriad Pro", sans-serif; }

  .brand-icon {
    position: absolute; left: 17px; top: 8px; width: 141px; height: 141px;
    background: linear-gradient(135deg, var(--sky) 0%, var(--sky) 55%, var(--deep-blue) 100%);
  }

  .slide {
    position: absolute; left: 31px; top: 170px; width: 1154px; height: 648px;
    background:
      radial-gradient(ellipse at 60% 30%, var(--paper-light) 0%, transparent 60%),
      linear-gradient(160deg, #e9e9e9 0%, var(--paper-mid) 55%, #e2e2e2 100%);
    overflow: hidden;
  }

  .image-frame {
    position: absolute; left: 29px; top: 34px; width: 480px; height: 424px;
    background: var(--charcoal);
  }
  .image-placeholder {
    position: absolute; left: 11px; top: 14px; width: 400px; height: 398px;
    background: linear-gradient(135deg, var(--sky) 0%, var(--sky) 50%, var(--deep-blue) 100%);
  }
  .image-caption {
    position: absolute; left: 446px; top: 212px;
    transform: translate(-50%, -50%) rotate(-90deg);
    white-space: nowrap;
    font-family: "Arimo", Arial, sans-serif; font-size: 23px; color: var(--white);
  }

  .page-tab { position: absolute; right: 16px; top: 13px; width: 102px; height: 102px; }
  .page-number {
    position: absolute; right: 28px; top: 31px;
    font-family: "Graduate", serif; font-size: 21px; color: var(--white);
  }

  .title-bar {
    position: absolute; left: 16px; top: 492px; width: 1122px; height: 144px;
    background: var(--charcoal);
  }
  .slide-title {
    position: absolute; left: 25px; top: 12px;
    font-family: "Graduate", serif; font-weight: 400; font-size: 66px; line-height: 1;
    color: var(--sky); letter-spacing: 1px; white-space: nowrap;
  }
  .title-rule {
    position: absolute; left: 25px; top: 90px; width: 420px; height: 3px; background: var(--white);
  }
  .slide-details {
    position: absolute; left: 80px; top: 103px;
    font-size: 19px; color: var(--white); white-space: nowrap;
  }
  .contact {
    position: absolute; right: 173px; top: 58px; text-align: right;
    font-size: 12px; line-height: 16px; color: var(--white);
  }
  .logo-box {
    position: absolute; right: 11px; top: 12px; width: 147px; height: 122px;
    background: var(--white);
    display: flex; align-items: center; justify-content: center;
  }
  .logo-name {
    font-family: "Source Sans 3", sans-serif; font-weight: 600; font-size: 52px;
    color: var(--logo-blue); letter-spacing: 1px;
  }
</style>
</head>
<body>
  <div class="brand-icon" role="img" aria-label="Brand icon illustration: blue square tile with a white mascot shape"></div>

  <main class="slide">
    <section class="image-frame">
      <div class="image-placeholder" role="img" aria-label="Sample image: blue tile with a white mascot illustration"></div>
      <p class="image-caption">sample image placement</p>
    </section>

    <svg class="page-tab" viewBox="0 0 102 102" aria-hidden="true">
      <polygon points="0,0 102,0 102,102" fill="var(--sky)"/>
    </svg>
    <span class="page-number">02</span>

    <footer class="title-bar">
      <h1 class="slide-title">SLIDE TITLE</h1>
      <div class="title-rule"></div>
      <p class="slide-details">DETAILS OF SLIDE / NAME OF PRESENTOR</p>
      <p class="contact">WWW.COMPANYSITE.COM<br>COMPANY@COMPANY.COM</p>
      <div class="logo-box"><span class="logo-name">TRV</span></div>
    </footer>
  </main>
</body>
</html>
```